Tellborne Medical

Need smart and sleek business cards design for my medical distribution company. use logos attached.

add my details

Lorcan Pettifer
Director/Sales Agent
lorcan@tellbornemedical-example.com.au
0491 638 170

```html
<!DOCTYPE html>
<html lang="en">
<head>
<meta charset="utf-8">
<title>Tellborne Medical – Business Cards</title>
<link href="https://fonts.googleapis.com/css2?family=Montserrat:wght@400;600;700&family=Roboto:wght@400&display=swap" rel="stylesheet">
<style>
  :root {
    --navy: #022460;
    --sky: #2a86bf;
    --paper: #ffffff;
    --ink: #111111;
    --backdrop: #6b6b6b;
  }
  html, body {
    margin: 0;
    padding: 0;
    overflow: hidden;
  }
  .canvas {
    position: relative;
    width: 1200px;
    height: 900px;
    background: var(--backdrop);
    overflow: hidden;
  }
  .card {
    position: absolute;
    border-radius: 14px;
    overflow: hidden;
  }
  .card-front {
    left: 62px;
    top: 110px;
    width: 378px;
    height: 662px;
    background: var(--paper);
  }
  .card-back {
    left: 477px;
    top: 262px;
    width: 661px;
    height: 377px;
    background: var(--navy);
    display: flex;
    align-items: center;
    justify-content: center;
  }
  .wordmark {
    font-family: "Montserrat", sans-serif;
    font-weight: 700;
    color: var(--navy);
    text-transform: uppercase;
    line-height: 1;
    text-align: center;
  }
  .front-wordmark {
    position: absolute;
    top: 58px;
    left: 0;
    right: 0;
    font-size: 26px;
    letter-spacing: 1px;
  }
  .front-wordmark .sub {
    display: block;
    font-size: 17px;
    letter-spacing: 6px;
    margin-top: 6px;
  }
  .back-wordmark {
    color: var(--paper);
    font-size: 76px;
    letter-spacing: 2px;
  }
  .back-wordmark .sub {
    display: block;
    font-size: 40px;
    letter-spacing: 16px;
    margin-top: 8px;
  }
  .person {
    position: absolute;
    top: 160px;
    left: 0;
    right: 0;
    text-align: center;
    font-family: "Montserrat", sans-serif;
  }
  .person-name {
    margin: 0;
    font-size: 24px;
    font-weight: 700;
    color: var(--navy);
    text-transform: uppercase;
  }
  .person-role {
    margin: 8px 0 0;
    font-size: 17px;
    font-weight: 400;
    color: var(--sky);
    text-transform: uppercase;
  }
  .contact {
    position: absolute;
    top: 262px;
    left: 0;
    right: 0;
    margin: 0;
    padding: 0;
    list-style: none;
    font-family: "Roboto", sans-serif;
    font-size: 17px;
    color: var(--ink);
    text-align: center;
  }
  .contact li {
    display: flex;
    align-items: center;
    justify-content: center;
    gap: 7px;
    height: 28px;
  }
  .contact svg { flex: none; }
  .email { font-size: 16px; letter-spacing: -0.2px; }
  .front-feature {
    position: absolute;
    left: 46px;
    right: 32px;
    bottom: 28px;
    height: 220px;
    color: var(--navy);
    font-size: 44px;
    text-align: left;
    line-height: 1;
  }
  .front-feature .mark {
    display: block;
    width: 130px;
    height: 130px;
    margin-bottom: 30px;
    background: var(--sky);
  }
</style>
</head>
<body>
<main class="canvas">
  <section class="card card-front" aria-label="Business card front">
    <div class="wordmark front-wordmark">Tellborne<span class="sub">Medical</span></div>

    <div class="person">
      <h1 class="person-name">Lorcan Pettifer</h1>
      <p class="person-role">Director/Sales Agent</p>
    </div>

    <ul class="contact">
      <li>
        <svg width="18" height="14" viewBox="0 0 18 14" aria-hidden="true">
          <path d="M1 5 C1 1 17 1 17 5 L13 5 L12 3 L6 3 L5 5 Z" fill="var(--sky)"/>
          <path d="M4 6 L14 6 L16 13 L2 13 Z" fill="var(--sky)"/>
          <circle cx="9" cy="9.5" r="2" fill="var(--paper)"/>
        </svg>
        <span>0491 638 170</span>
      </li>
      <li class="email">
        <svg width="21" height="14" viewBox="0 0 21 14" aria-hidden="true">
          <rect x="0.5" y="0.5" width="20" height="13" fill="var(--sky)"/>
          <path d="M1 1 L10.5 8 L20 1 M1 13 L8 6.5 M20 13 L13 6.5" stroke="var(--paper)" stroke-width="1.2" fill="none"/>
        </svg>
        <span>lorcan@tellbornemedical-example.com.au</span>
      </li>
    </ul>

    <div class="wordmark front-feature" aria-hidden="true">
      <span class="mark"></span>Tellborne
    </div>
  </section>

  <section class="card card-back" aria-label="Business card back">
    <div class="wordmark back-wordmark">Tellborne<span class="sub">Medical</span></div>
  </section>
</main>
</body>
</html>
```